Business card design needed to incorporate existing logo

We need a business card for a new modern Accounting & Business Solutions company call Kelvra Partners.com.au servicing all of Australia.
My tagline is Steady Ledger Answers... done right.

We specialise in Cloud Accounting and this is our primary focus. We also provide tax representation, debt recovery, computer, tablet and smart phone sales.

I would like a design that uses my corporate, trustworthy colours of blue/white, black/grey however am open to suggestion. I have attached my logo to go on the card somewhere,of which you will see the colour scheme.

I am after a card that STANDS OUT, somewhere between it not being too busy and not being a baron waste of space.

A 'cloud' incorporated in the design may work well, up to your artistic judgement. I know what I like when I see it; it is harder to put into words!

Excited to see your ideas!
I have added my logo predominately (blue/white) and for additional opportunity have added my reverse logo (darker one). I have used the blue/white on my website and letterhead. I will be using both on my vehicle signage.

Target Market(s)

Tradesmen and small-medium businesses of all descriptions Australia-wide

Industry/Entity Type

Debt

Contact Information for Business Card

Dale Fenwick
Principal (optional)
Kelvra Partners.com.au
Steady Ledger Answers... done right

P: 1800 530 918
M: 0418 652 074 (optional)
W: www.kelvrapartners.example
E: admin@kelvrapartners.example

Logo Text

Steady Ledger Answers... done right!

Logo styles of interest
Wordmark Logo
Requirements
Must have
• Must look professional and of high quality not cheap.

My logo and my tagline 'Steady Ledger Answers... done right'.

I have my colourscheme in mind as per my attached logo, however am open to suggestion. I want to see what you can create that I would not have thought of.

Modern, innovative.
Something I won't look at and think, 'I could have done that myself'.

Must be able to be printed on Plimo 300gm premium cards and the artwork provided to me.
Nice to have
• Title of Principal is optional depending on space and judement call of look/fee.
M: (mobile) number is also optional as above.

Somthing cloud related given the Cloud Accounting aspect may be relevant. I leave it to your artistic design and judgement.
Should not have
• Must not look cheap.

```html
<!DOCTYPE html>
<html lang="en">
<head>
<meta charset="utf-8">
<title>Kelvra Partners – Business Card</title>
<link rel="stylesheet" href="https://fonts.googleapis.com/css2?family=Poppins:wght@600&family=Questrial&display=swap">
<style>
  :root {
    --navy: #0b1565;
    --navy-ink: #0f1a6c;
    --brand-blue: #3d8fe2;
    --tagline: #dbe6f6;
    --mark-fill: #4a9ce8;
    --card-light: #ffffff;
    --card-grey: #c9cfd1;
    --ink: #111318;
  }
  * { margin: 0; padding: 0; box-sizing: border-box; }
  html, body {
    width: 1200px;
    height: 720px;
    overflow: hidden;
    background: #ffffff;
  }
  .card {
    position: relative;
    width: 1200px;
    height: 720px;
    overflow: hidden;
    font-family: "Questrial", "Helvetica Neue", Arial, sans-serif;
  }
  .brand-panel {
    position: absolute;
    left: 0; top: 0;
    width: 594px;
    height: 720px;
    background: var(--navy);
    z-index: 2;
    box-shadow: 10px 0 18px rgba(0, 0, 0, 0.28);
  }
  .brand-dot {
    position: absolute;
    left: 121px;
    top: 132px;
    width: 288px;
    height: 288px;
    border-radius: 50%;
    background: var(--mark-fill);
  }
  .brand-name {
    position: absolute;
    left: 41px;
    top: 442px;
    font-size: 41px;
    line-height: 1;
    color: var(--brand-blue);
    white-space: nowrap;
  }
  .brand-tagline {
    position: absolute;
    left: 41px;
    top: 493px;
    font-size: 25px;
    line-height: 1;
    color: var(--tagline);
    white-space: nowrap;
  }
  .info-panel {
    position: absolute;
    left: 594px; top: 0;
    width: 606px;
    height: 720px;
    background: radial-gradient(ellipse 620px 560px at 100% 42%, var(--card-light) 0%, #eef0f0 40%, var(--card-grey) 100%);
  }
  .person-name {
    position: absolute;
    right: 26px;
    top: 84px;
    font-family: "Poppins", "Helvetica Neue", Arial, sans-serif;
    font-weight: 600;
    font-size: 41px;
    line-height: 1;
    color: var(--navy-ink);
    white-space: nowrap;
  }
  .person-title {
    position: absolute;
    left: 308px;
    top: 139px;
    font-size: 26px;
    line-height: 1;
    color: var(--ink);
  }
  .contact-list {
    position: absolute;
    left: 30px;
    top: 530px;
    list-style: none;
    font-size: 26px;
    line-height: 36px;
    color: var(--ink);
  }
  .contact-label {
    display: inline-block;
    width: 42px;
    font-weight: 700;
  }
</style>
</head>
<body>
<main class="card">
  <section class="brand-panel">
    <div class="brand-dot"></div>
    <p class="brand-name">Kelvra Partners.com.au</p>
    <p class="brand-tagline">Steady Ledger Answers... done right</p>
  </section>
  <section class="info-panel">
    <h1 class="person-name">Dale Fenwick</h1>
    <p class="person-title">Principal</p>
    <ul class="contact-list">
      <li><span class="contact-label">P :</span>1800 530 918</li>
      <li><span class="contact-label">M:</span>0418 652 074</li>
      <li><span class="contact-label">E :</span>admin@kelvrapartners.example</li>
    </ul>
  </section>
</main>
</body>
</html>
```